Drapery & Decor Atelier Project…
I am looking for a new website design for a store front “Drapery & Decor Atelier” business. Their customer would walk in off the street to have curtains designed for their home or business. This is not an ecommerce website.
The website colors should be light blue, dark blue, white and maybe tan. Be creative.
The curtains they sell can be found at www.plvexo.example and www.dombly.example. Please use images from these two website.
Navigation:
Home
Our Studio
Our Services
Our Manufactures
PLVEXO
Dombly
Our Process
Testimonials
Refer a Client
Subscribe to our Newsletter
Our Blog – (Needed for Internet Marketing)
Contact Us
The website should have a large footer for internet marketing purposes.
Updates
Great designs. Thank you everyone. I have sent them all to the client and i am waiting for feedback. I will let everyone know as soon as possible.
Sorry for the delay everyone. The client has been on vacation and has not provided feedback yet. As soon as I have an update I will let everyone know.

```html
<!DOCTYPE html>
<html lang="en">
<head>
<meta charset="utf-8">
<title>Drapery &amp; Decor Atelier</title>
<link href="https://fonts.googleapis.com/css2?family=Signika:wght@400;600;700&family=Arimo:wght@400;700&family=Great+Vibes&display=swap" rel="stylesheet">
<style>
:root{
  --backdrop:#2c2a29;
  --page:#ffffff;
  --ink:#3a3a3a;
  --body:#555555;
  --teal:#1a9bbf;
  --teal-dark:#11809f;
  --navy:#1d3f6e;
  --navy-dark:#142d50;
  --tan:#c4a27a;
  --tan-light:#f3ebe0;
  --nav-top:#5a5a5a;
  --nav-bottom:#262626;
  --panel:#efefef;
  --footer:#2a2a2a;
  --green:#5aa628;
}
*{margin:0;padding:0;box-sizing:border-box}
html,body{width:900px;height:1200px;overflow:hidden;background:var(--backdrop)}
body{font-family:"Arimo",Arial,sans-serif;color:var(--body);position:relative}
.abs{position:absolute}
.page{position:absolute;left:70px;top:0;width:756px;height:956px;background:var(--page)}

/* header */
.brand{left:102px;top:24px;font-family:"Signika",sans-serif;font-weight:700;color:#3b3b3b;font-size:22px;line-height:26px}
.brand small{display:block;font-size:13px;line-height:16px;color:#3b3b3b}
.top-links{left:620px;top:30px;font-size:9px;color:#555;word-spacing:2px}
.search{left:343px;top:49px;width:234px;height:30px;background:#e4e4e4;border-radius:4px}
.search .field{position:absolute;left:5px;top:5px;width:180px;height:20px;background:#fff;border:1px solid #ccc;font-size:9px;color:#999;padding:5px 4px}
.search .go{position:absolute;left:189px;top:5px;width:41px;height:20px;background:var(--teal);border-radius:2px;color:#fff;font-size:10px;text-align:center;line-height:20px}
.consult{left:610px;top:51px;width:188px;height:27px;background:linear-gradient(var(--navy),var(--navy-dark));border-radius:3px;color:#fff;font-size:10px;line-height:27px;padding-left:26px}
.consult svg{position:absolute;left:8px;top:7px}

.nav{left:70px;top:104px;width:756px;height:26px;background:linear-gradient(var(--nav-top),var(--nav-bottom))}
.nav ul{list-style:none;display:flex;height:26px;padding-left:40px}
.nav li{font-size:8px;font-weight:700;color:#fff;line-height:26px;padding:0 15px;border-right:1px solid #1d1d1d}
.nav li.active{background:var(--teal);padding:0 12px;height:29px;margin-top:-3px;line-height:32px}
.nav li:last-child{border:none}

/* hero */
.hero{left:88px;top:146px;width:720px;height:274px;border:1px solid #ddd;background:#fafafa}
.hero-img{top:6px;height:262px}
.hero-1{left:7px;width:211px;background:linear-gradient(135deg,#6d6248,#b7a987 55%,#4f5a4a)}
.hero-2{left:218px;width:228px;background:linear-gradient(160deg,#e9e6ee,#cbb9d1 55%,#f1eef4)}
.hero-3{left:446px;width:265px;background:linear-gradient(180deg,#7d6a58,#c9c4bd 45%,#8f8f9f 75%,#6d4a33)}
.hero-card{left:38px;top:41px;width:288px;height:182px;background:rgba(255,255,255,.82);border-radius:6px;padding:14px 12px}
.hero-card h1{font-family:"Signika",sans-serif;font-weight:400;font-size:23px;color:#444}
.hero-card h1 b{color:var(--teal);font-weight:600}
.hero-card p{font-size:9px;line-height:15px;letter-spacing:.5px;color:#444;margin-top:10px}
.hero-btn{left:165px;top:143px;width:98px;height:23px;border-radius:4px;background:var(--navy);color:#fff;font-family:"Signika",sans-serif;font-size:13px;line-height:23px;padding-left:10px}
.hero-btn i{position:absolute;right:7px;top:6px;width:11px;height:11px;border-radius:50%;background:#fff}
.hero-btn i:after{content:"";position:absolute;left:4px;top:3px;border-left:4px solid var(--navy);border-top:2.5px solid transparent;border-bottom:2.5px solid transparent}
.badge{left:306px;top:30px;width:60px;height:60px;border-radius:50%;background:radial-gradient(#3fb6e0,#1683b7);color:#fff;font-family:"Signika",sans-serif;font-weight:700;font-size:12px;line-height:13px;text-align:center;padding-top:17px;transform:rotate(-20deg)}

/* content */
.intro{left:106px;top:450px;width:500px}
.intro h2{font-family:"Signika",sans-serif;font-weight:700;font-size:24px;color:#444}
.intro h3{font-family:"Signika",sans-serif;font-weight:600;font-size:13px;color:var(--teal);margin-top:2px}
.intro p{font-size:8.6px;line-height:13.6px;letter-spacing:.3px;color:#555;margin-top:9px}

.features{left:106px;top:648px}
.feature{position:absolute;top:0;width:150px}
.feature h4{font-family:"Signika",sans-serif;font-weight:400;font-size:15px;color:#444;padding-left:24px;height:20px;line-height:20px;position:relative}
.feature h4 svg{position:absolute;left:0;top:0}
.feature p{font-size:8.6px;line-height:13.6px;letter-spacing:.3px;color:#555;margin-top:12px}
.sep{top:648px;width:0;height:100px;border-left:1px dotted #aaa}

/* featured panel */
.featured{left:622px;top:443px;width:188px;height:321px;background:var(--panel);border:1px solid #ddd}
.featured h5{font-family:"Great Vibes",cursive;font-weight:400;font-size:25px;color:var(--teal-dark);padding:6px 0 0 14px;height:40px;background:linear-gradient(#fafafa,#e3e3e3)}
.feat-img{left:11px;top:52px;width:165px;height:100px;background:linear-gradient(90deg,#f4f4f4 20%,#5f86b8 30%,#2c5288 60%,#7ea3cf 75%,#f4f4f4 85%)}
.feat-more{left:11px;top:134px;width:165px;height:18px;background:rgba(60,60,60,.7);color:#fff;font-size:9px;text-align:right;padding:4px 5px}
.feat-text{left:13px;top:159px;font-size:9px;line-height:13px;color:#333;width:170px}
.btn-navy,.btn-dark{top:190px;height:18px;border-radius:3px;color:#fff;font-size:10px;line-height:18px;text-align:center}
.btn-navy{left:13px;width:56px;background:var(--navy)}
.btn-dark{left:126px;width:42px;background:#333}
.hours{left:11px;top:222px;width:167px;height:44px;border:1px solid var(--tan);background:linear-gradient(#fbf7f1,var(--tan-light))}
.hours svg{position:absolute;left:12px;top:4px}
.hours b{position:absolute;left:52px;top:6px;font-family:"Signika",sans-serif;font-size:11px;color:#222}
.hours strong{position:absolute;left:52px;top:20px;font-family:"Signika",sans-serif;font-size:15px;color:var(--navy)}
.listing{top:277px;width:84px;height:24px;border-radius:2px}
.listing.a{left:9px;background:#6d7784}
.listing.b{left:97px;background:#fff;border:1px solid #ccc}

/* gallery */
.gallery{left:89px;top:778px;width:717px;height:129px;background:var(--panel)}
.thumb{top:8px;width:150px;height:110px}
.t1{left:27px;background:linear-gradient(135deg,#d8d0bd,#9e8f6e 60%,#5c5342)}
.t2{left:203px;background:linear-gradient(135deg,#27406b,#4d67a0 50%,#1a2745)}
.t3{left:372px;background:linear-gradient(135deg,#3a3a3a,#c44266 40%,#e58aa4 70%,#2d2d2d)}
.t4{left:541px;background:linear-gradient(135deg,#d9b57a,#c01c4c 50%,#8e1437)}
.arrow{top:50px}

/* footer */
.footer{left:70px;top:956px;width:756px;height:136px;background:var(--footer)}
.social-tab{left:70px;top:920px}
.social-label{left:137px;top:942px;font-family:"Signika",sans-serif;font-weight:600;font-size:14px;color:#fff}
.social-dot{top:940px;width:18px;height:18px;border-radius:3px;background:#6f93b8}
.subscribe{left:146px;top:983px;font-family:"Signika",sans-serif;font-weight:600;font-size:11px;color:#ddd}
.mail-field{left:144px;top:1004px;width:176px;height:19px;border-radius:10px;background:linear-gradient(#d0d0d0,#8c8c8c);font-style:italic;font-weight:700;font-size:9px;color:#444;padding:4px 10px}
.mail-field svg{position:absolute;right:8px;top:4px}
.copy-box{left:137px;top:1046px;width:183px;height:46px;background:#222;border-radius:12px 12px 0 0;font-size:8px;line-height:15px;color:#ddd;padding:9px 0 0 43px}
.copy-box i{position:absolute;left:12px;top:12px;width:22px;height:22px;border-radius:50%;border:3px solid #ccc}
.nav-head{left:382px;top:971px;font-family:"Signika",sans-serif;font-weight:600;font-size:16px;color:#fff;letter-spacing:.5px}
.fnav{top:998px;list-style:none;font-size:9.5px;line-height:16.6px;color:#eee}
.fnav li:before{content:"";display:inline-block;border-left:5px solid var(--tan);border-top:3px solid transparent;border-bottom:3px solid transparent;margin-right:6px}
.contact{right:94px;top:970px;text-align:right;font-size:9.5px;line-height:15.2px;color:#fff;font-style:normal}
.contact h6{font-family:"Signika",sans-serif;font-weight:400;font-size:14px;color:var(--tan);margin-bottom:6px}
.contact b{font-size:11px}
.strip{left:70px;top:1092px;width:756px;height:54px;background:#3a3a3a}
.strip-name{left:90px;top:1106px;font-family:"Signika",sans-serif;font-size:16px;color:#ddd}
.partners{left:332px;top:1101px;width:474px;height:34px;background:#fff;display:flex;align-items:center;justify-content:space-around;padding:0 8px}
.partners span{display:block;width:40px;height:12px;background:#8a8a8a;border-radius:2px}
.legal{left:70px;top:1148px;width:756px;text-align:center;font-size:7.6px;line-height:12px;color:#c9c9c9;letter-spacing:.2px}
</style>
</head>
<body>
<div class="page"></div>

<header>
  <div class="abs brand">Drapery &amp; Decor<small>Atelier Project</small></div>
  <div class="abs top-links">My Account &nbsp;|&nbsp; Our Blog &nbsp;|&nbsp; Contact Us</div>
  <div class="abs search"><div class="field">Enter Keyword or item#</div><div class="go">Search</div></div>
  <div class="abs consult">
    <svg width="13" height="13" viewBox="0 0 13 13"><rect x="0.8" y="2" width="11.4" height="10" rx="1" fill="none" stroke="#fff" stroke-width="1.4"/><path d="M0.8 5h11.4M4 0.5v3M9 0.5v3" stroke="#fff" stroke-width="1.4"/></svg>
    Book a consultation | Saved designs
  </div>
</header>

<nav class="abs nav">
  <ul>
    <li class="active">HOME</li><li>OUR STUDIO</li><li>OUR SERVICES</li><li>OUR MANUFACTURES</li><li>PLVEXO</li><li>DOMBLY</li><li>OUR PROCESS</li>
  </ul>
</nav>

<section class="abs hero">
  <div class="abs hero-img hero-1" role="img" aria-label="Patterned drapery fabric close-up"></div>
  <div class="abs hero-img hero-2" role="img" aria-label="Floral printed cushions and linen"></div>
  <div class="abs hero-img hero-3" role="img" aria-label="Furnished living room with armchair and lamp"></div>
  <div class="abs hero-card">
    <h1>Curtains &amp; <b>Curtain Rods.</b></h1>
    <p><b>Delay the arrival</b> of dawn with curtains that block, soften or change the colour of the sunlight and bring a new mood to every room Delay the arrival of dawn with curtains that block, soften or change the colour of the sunlight a new mood to every room.</p>
    <div class="abs hero-btn">Book a Visit<i></i></div>
  </div>
  <div class="abs badge">VISIT<br>US</div>
</section>

<section class="abs intro">
  <h2>Curtains</h2>
  <h3>Ashford, Millbrook, The Greenvale &amp; Westmoor.</h3>
  <p>At Harold Vance Interiors we have an experienced and fully qualified interior designer who can help you obtain the professionally styled room that you have always wanted to have. Our interior designer will find you the right curtains, blinds and soft furnishings as detailed below that combine to create a remarkable interior design.</p>
  <p style="margin-top:13px">As well as supplying and installing various types of flooring to customers we can supply you with soft furnishings, curtains, blinds and more for the home. All of our interior furnishings are of the highest quality and are produced by some of the worlds top brands. Browse through our galleries below to get a taste of what we can offer, or visit one of our manufacturer's websites for more information.</p>
</section>

<section class="abs features">
  <div class="feature" style="left:0">
    <h4><svg width="20" height="18" viewBox="0 0 20 18"><path d="M1 9l6 6L19 2" fill="none" stroke="#5aa628" stroke-width="4" stroke-linecap="round"/></svg>Best Privacy</h4>
    <p>Easy to hang, use and take down, useable on 100% of all existing tracks.Our disposable curtains are designed.</p>
  </div>
  <div class="feature" style="left:168px;top:-3px">
    <h4><svg width="20" height="18" viewBox="0 0 20 18"><path d="M1 9l6 6L19 2" fill="none" stroke="#5aa628" stroke-width="4" stroke-linecap="round"/></svg>Best Protection</h4>
    <p>Easy to hang, use and take down, useable on 100% of all existing tracks.Our disposable curtains are designed.</p>
  </div>
  <div class="feature" style="left:337px;top:-3px">
    <h4><svg width="20" height="18" viewBox="0 0 20 18"><path d="M1 9l6 6L19 2" fill="none" stroke="#5aa628" stroke-width="4" stroke-linecap="round"/></svg>Best Price</h4>
    <p>Easy to hang, use and take down, useable on 100% of all existing tracks.Our disposable curtains are designed.</p>
  </div>
</section>
<div class="abs sep" style="left:259px"></div>
<div class="abs sep" style="left:429px"></div>

<aside class="abs featured">
  <h5>Featured Fabrics</h5>
  <div class="abs feat-img" role="img" aria-label="Blue patterned curtain panels on a rod"></div>
  <div class="abs feat-more">View more [+]</div>
  <div class="abs feat-text">Lorem Ipsum is simply dummy text of the printing and typesetting industry</div>
  <div class="abs btn-navy">Enquire</div>
  <div class="abs btn-dark">More</div>
  <div class="abs hours">
    <svg width="34" height="34" viewBox="0 0 34 34"><circle cx="17" cy="17" r="15" fill="#222"/><circle cx="17" cy="17" r="12" fill="#fff"/><path d="M17 8v9l6 4" stroke="#222" stroke-width="2" fill="none"/></svg>
    <b>Studio Open Today</b>
    <strong>9:00 – 17:30</strong>
  </div>
  <div class="abs listing a"></div>
  <div class="abs listing b"></div>
</aside>

<section class="abs gallery">
  <svg class="abs arrow" style="left:4px" width="20" height="28" viewBox="0 0 20 28"><path d="M16 2L4 14l12 12" fill="none" stroke="#777" stroke-width="5"/></svg>
  <div class="abs thumb t1" role="img" aria-label="Upholstered armchair beside a window"></div>
  <div class="abs thumb t2" role="img" aria-label="Navy and white patterned fabric"></div>
  <div class="abs thumb t3" role="img" aria-label="Folded fabric swatches in pinks and neutrals"></div>
  <div class="abs thumb t4" role="img" aria-label="Crimson embroidered drapery fabric"></div>
  <svg class="abs arrow" style="left:694px" width="20" height="28" viewBox="0 0 20 28"><path d="M4 2l12 12L4 26" fill="none" stroke="#777" stroke-width="5"/></svg>
</section>

<footer>
  <svg class="abs social-tab" width="756" height="37" viewBox="0 0 756 37">
    <rect x="0" y="30" width="756" height="7" fill="#8c8c8c"/>
    <path d="M38 37 C50 37 52 6 72 6 H300 C320 6 322 37 334 37 Z" fill="#2a2a2a" stroke="#8c8c8c" stroke-width="3"/>
  </svg>
  <div class="abs footer"></div>
  <div class="abs social-label">Socialize with us:</div>
  <div class="abs social-dot" style="left:262px"></div>
  <div class="abs social-dot" style="left:289px"></div>
  <div class="abs social-dot" style="left:316px"></div>
  <div class="abs social-dot" style="left:344px"></div>

  <div class="abs subscribe">Subscribe to our Newsletter</div>
  <div class="abs mail-field">Your E-Mail Address
    <svg width="16" height="11" viewBox="0 0 16 11"><rect x="0.5" y="0.5" width="15" height="10" fill="#eee" stroke="#777"/><path d="M1 1l7 5 7-5" fill="none" stroke="#777"/></svg>
  </div>
  <div class="abs copy-box"><i></i>@ 2012 Drapery &amp; Decor Atelier<br>All Right Reserved.</div>

  <div class="abs nav-head">Navigation</div>
  <ul class="abs fnav" style="left:380px">
    <li>Home</li><li>Our Studio</li><li>Our Services</li><li>Our Manufactures</li><li>PLVEXO Dombly</li>
  </ul>
  <ul class="abs fnav" style="left:496px">
    <li>Our Process</li><li>Testimonials</li><li>Refer a Client</li><li>Our Blog</li><li>Contact Us</li>
  </ul>

  <address class="abs contact">
    <h6>CONTACT INFORMATION</h6>
    <b>Brindle's Corner Shop</b><br>14 Larkspur Lane<br>Eastland<br>
    <b>4Hr. Tel. :</b> 08 5550 1947<br>
    <b>Email:</b> hello@brindlecorner.example
  </address>

  <div class="abs strip"></div>
  <div class="abs strip-name">Drapery &amp; Decor Atelier Project</div>
  <div class="abs partners"><span></span><span></span><span></span><span></span><span></span><span></span><span></span><span></span><span></span></div>

  <div class="abs legal">
    Wood Flooring | About Us | Curtains, Blinds &amp; Furnishings | Curtain Makers | Curtains | Roman Blinds | Interior Design | Wooden Flooring | Laminate | Carpets | Larwood &amp; Fennick |<br>
    Commercial | Testimonials | Floor Preparation | Gallery | Kitchens and Bathrooms | Contact Us | Resources | Sitemap | XML Sitemap<br>
    © Copyright 2012 - Drapery &amp; Decor Atelier Project - All Rights Reserved - Privacy &amp; Cookies Policy - Wood Flooring Ashford - Company No. 04812736
  </div>
</footer>
</body>
</html>
```